Ultra Distance Charity Bike Ride.

Hello.

I need a business card to pass to people whilst out on my charity bike ride.

I’m raising funds/awareness about mental health. My funds are going to Harbor Light. I have a link to my donation page in my instagram bio. My instagram page will also be a source for people to follow my adventures. My Instagram page is tomwelsk.

I would like to have this card not for just one trip, I’d like it to be something that I can use on future endeavors.

```html
<!DOCTYPE html>
<html lang="en">
<head>
<meta charset="utf-8">
<title>Tom Welsk – Charity Ride Card</title>
<link rel="stylesheet" href="https://fonts.googleapis.com/css2?family=Open+Sans:wght@400;700&display=swap">
<style>
  :root {
    --page: #e9e9e7;
    --card-white: #f3f3f3;
    --teal: #2fa6c6;
    --teal-deep: #2596b8;
    --teal-light: #49b6d2;
    --sun: #f0b63c;
    --rose: #e63772;
    --ink-white: #ffffff;
  }
  * { box-sizing: border-box; margin: 0; padding: 0; }
  html, body {
    width: 1200px; height: 800px; overflow: hidden;
    background: var(--page);
    font-family: "Open Sans", Arial, sans-serif;
  }
  .canvas {
    width: 1200px; height: 800px;
    display: flex; align-items: center; justify-content: center; gap: 40px;
  }
  .card {
    position: relative;
    width: 550px; height: 314px;
    overflow: hidden;
    box-shadow: 0 6px 18px rgba(0,0,0,0.12);
  }

  /* Front */
  .card-front { background: var(--card-white); }
  .card-front .corner-art { position: absolute; inset: 0; }
  .brand {
    display: flex; align-items: center; gap: 12px;
    color: var(--teal-deep); font-weight: 400; white-space: nowrap;
  }
  .brand-dot { border-radius: 50%; background: var(--teal); flex: none; }
  .front-lockup {
    position: absolute; left: 0; right: 0; top: 50%;
    transform: translateY(-50%);
    display: flex; flex-direction: column; align-items: center; gap: 10px;
  }
  .card-front .brand { font-size: 38px; letter-spacing: 0.5px; }
  .card-front .brand-dot { width: 22px; height: 22px; }
  .front-tagline {
    font-size: 15px; color: var(--teal-deep); letter-spacing: 0.3px;
  }

  /* Back */
  .card-back { background: var(--teal); }
  .card-back .sheen { position: absolute; inset: 0; }
  .white-panel {
    position: absolute; left: 0; bottom: 0;
    width: 218px; height: 188px;
    background: var(--card-white);
  }
  .mark-area {
    position: absolute; left: 180px; top: 112px;
    width: 118px; height: 176px; border-radius: 18px;
    background: linear-gradient(135deg, var(--rose) 0%, #ee7a5a 55%, var(--sun) 100%);
    opacity: 0.9;
  }
  .card-back .brand {
    position: absolute; left: 22px; top: 214px;
    font-size: 17px; gap: 8px;
  }
  .card-back .brand-dot { width: 11px; height: 11px; }
  .identity {
    position: absolute; left: 252px; top: 28px; color: var(--ink-white);
  }
  .identity .name { font-size: 27px; font-weight: 700; letter-spacing: 0.5px; line-height: 1.15; }
  .identity .role { font-size: 15px; font-weight: 400; margin-left: 20px; }
  .contacts {
    position: absolute; left: 330px; top: 118px;
    list-style: none; color: var(--ink-white); font-size: 14px;
  }
  .contacts li { display: flex; align-items: center; gap: 10px; height: 30px; white-space: nowrap; }
  .contacts svg { width: 15px; height: 15px; fill: var(--ink-white); flex: none; }
</style>
</head>
<body>
<main class="canvas">

  <section class="card card-front" aria-label="Card front">
    <svg class="corner-art" viewBox="0 0 550 314" aria-hidden="true">
      <polygon points="500,0 550,0 550,95" fill="var(--teal)"/>
      <line x1="486" y1="0" x2="536" y2="95" stroke="var(--sun)" stroke-width="4"/>
      <polygon points="0,219 0,314 50,314" fill="var(--teal)"/>
      <line x1="14" y1="219" x2="64" y2="314" stroke="var(--sun)" stroke-width="4"/>
    </svg>
    <div class="front-lockup">
      <div class="brand"><span class="brand-dot"></span><span class="brand-name">Harbor Light</span></div>
      <p class="front-tagline">Riding for mental health</p>
    </div>
  </section>

  <section class="card card-back" aria-label="Card back">
    <svg class="sheen" viewBox="0 0 550 314" aria-hidden="true">
      <polygon points="300,0 420,0 550,130 550,250" fill="var(--teal-light)" opacity="0.35"/>
    </svg>
    <div class="white-panel"></div>
    <div class="mark-area" role="img" aria-label="Large decorative brand artwork"></div>
    <div class="brand"><span class="brand-dot"></span><span class="brand-name">Harbor Light</span></div>

    <div class="identity">
      <p class="name">TOM WELSK</p>
      <p class="role">Ultra Distance Charity Rider</p>
    </div>

    <ul class="contacts">
      <li>
        <svg viewBox="0 0 24 24" aria-hidden="true"><circle cx="12" cy="12" r="9" fill="none" stroke="#fff" stroke-width="2"/><circle cx="12" cy="12" r="3.5" fill="none" stroke="#fff" stroke-width="2"/></svg>
        <span>@tomwelsk</span>
      </li>
      <li>
        <svg viewBox="0 0 24 24" aria-hidden="true"><path d="M12 21s-8-5.2-8-11a4.5 4.5 0 0 1 8-2.8A4.5 4.5 0 0 1 20 10c0 5.8-8 11-8 11z"/></svg>
        <span>Donate via link in bio</span>
      </li>
      <li>
        <svg viewBox="0 0 24 24" aria-hidden="true"><circle cx="12" cy="12" r="9" fill="none" stroke="#fff" stroke-width="2"/><path d="M3 12h18M12 3c3 3 3 15 0 18M12 3c-3 3-3 15 0 18" fill="none" stroke="#fff" stroke-width="1.6"/></svg>
        <span>www.harborlight.org</span>
      </li>
      <li>
        <svg viewBox="0 0 24 24" aria-hidden="true"><path d="M5 18l4-10h6l4 10" fill="none" stroke="#fff" stroke-width="2"/><circle cx="5" cy="18" r="3" fill="none" stroke="#fff" stroke-width="2"/><circle cx="19" cy="18" r="3" fill="none" stroke="#fff" stroke-width="2"/></svg>
        <span>Follow the adventures</span>
      </li>
    </ul>
  </section>

</main>
</body>
</html>
```